Mortgage Broker Site

Need a custom design for a mortgage broker site - please refer to the attached Word .doc that gives more detail.

Number of Pages Required

5+ page

Colors

Designer to choose colors to be used in the design.

```html
<!DOCTYPE html>
<html lang="en">
<head>
<meta charset="utf-8">
<title>Homevale – Mortgage Broker</title>
<link href="https://fonts.googleapis.com/css2?family=Open+Sans:wght@300;400;600&display=swap" rel="stylesheet">
<style>
:root{
  --brand-red:#a30a2a;
  --ink:#111111;
  --muted:#666666;
  --white:#ffffff;
  --sky:#acd3ee;
  --violet:#7f52ad;
  --footer-blue:#3398dc;
  --sketch:#eeeeee;
}
*{margin:0;padding:0;box-sizing:border-box}
html,body{width:710px;height:1200px;overflow:hidden;background:var(--white)}
body{position:relative;font-family:'Open Sans',sans-serif;color:var(--ink)}
.abs{position:absolute}
.center{left:0;width:710px;text-align:center}

/* hero */
.hero{left:0;top:0;width:710px;height:377px;background:linear-gradient(100deg,#d9c7bd 0%,#e6b9a5 35%,#c98a70 60%,#b86a52 80%,#d99b82 100%)}
.hero-shade{left:0;top:0;width:710px;height:60px;background:linear-gradient(#1c1c1c,rgba(28,28,28,0))}
.brand{left:95px;top:30px;font-size:28px;font-weight:600;color:var(--white);line-height:1}
.brand-mark{left:238px;top:38px;width:8px;height:8px;background:var(--brand-red)}
.nav a{position:absolute;top:37px;height:17px;line-height:17px;font-size:8px;font-weight:600;color:var(--white);text-decoration:none}
.nav .active{background:var(--brand-red);padding:0 6px;left:273px;border-radius:1px}
.hero-title{left:94px;top:143px;font-size:20px;font-weight:600}
.hero-text{left:95px;top:174px;width:255px;font-size:8px;line-height:12px;font-weight:600;color:#222}
.btn{top:221px;height:25px;line-height:23px;font-size:7px;font-weight:600;text-align:center;border:1px solid var(--brand-red)}
.btn-solid{left:95px;width:80px;background:var(--brand-red);color:var(--white)}
.btn-line{left:184px;width:79px;color:var(--ink)}
.arrow{top:180px;width:22px;height:22px;border-radius:50%;background:#222}
.dots span{position:absolute;top:365px;height:2px;width:10px;background:#555}

/* tools */
.section-title{font-size:21px;font-weight:600}
.section-sub{font-size:8.4px;color:var(--muted)}
.card{top:473px;width:164px;height:88px;background:var(--white);box-shadow:0 1px 6px rgba(0,0,0,.1);text-align:center}
.card h3{margin-top:29px;font-size:10.5px;font-weight:400}
.card .rule{width:19px;height:1px;background:var(--brand-red);margin:6px auto 5px}
.card p{font-size:7px;font-weight:300;color:#444;line-height:11px}
.tool-icon{top:451px;width:44px;height:44px;border-radius:50%;background:var(--brand-red)}

/* limits */
.limits{left:0;top:589px;width:710px;height:139px;background:var(--sky)}
.limits-sub{top:644px;font-size:8.2px;color:#222;line-height:12px}
.search-input{left:245px;top:679px;width:166px;height:17px;background:var(--white);border:1px solid #ccc}
.search-btn{left:419px;top:679px;width:46px;height:17px;line-height:17px;background:var(--brand-red);color:var(--white);font-size:7px;font-weight:600;text-align:center}

/* connect */
.connect{left:0;top:728px;width:710px;height:139px;background:var(--violet)}
.connect-title{top:790px;font-size:21px;font-weight:600;color:var(--white);line-height:27px}

/* town */
.town{left:0;top:867px;width:710px;height:115px;background:linear-gradient(#ffffff,var(--sketch))}

/* footer */
.footer{left:0;top:982px;width:710px;height:218px;background:var(--footer-blue)}
.col{top:1010px;width:178px;text-align:center;color:var(--white)}
.col h4{font-size:8px;font-weight:600;margin-bottom:4px}
.col li{list-style:none;font-size:6.3px;line-height:14.5px}
.divider{top:1006px;width:1px;height:81px;background:var(--white)}
.social{top:1093px;width:16px;height:16px;border-radius:50%}
.scroll-top{left:337px;top:1123px;width:37px;height:37px;border-radius:50%;background:#111;color:var(--white);font-size:6px;font-weight:600;text-align:center;padding-top:10px;line-height:8px}
.legal{font-size:6.2px;color:#1a1a1a;line-height:9px}
</style>
</head>
<body>

<div class="abs hero" role="img" aria-label="Photo of a hand holding a house key on a small house keyring, blurred home behind"></div>
<div class="abs hero-shade"></div>
<div class="abs brand">Homevale</div>
<div class="abs brand-mark"></div>
<nav class="nav">
  <a class="active">Home</a>
  <a style="left:328px">Rates</a>
  <a style="left:377px">Purchase</a>
  <a style="left:439px">Refinance</a>
  <a style="left:504px">Schedule a Call</a>
  <a style="left:589px">Guides</a>
</nav>
<h1 class="abs hero-title">Homevale has a soltion for you</h1>
<p class="abs hero-text">Lorem ipsum dolor sit amet, consectetur adipisicing elit, sed do eiusmod tempor incididunt ut labore et dolore magna aliqua. Ut enim ad minim veniam,</p>
<div class="abs btn btn-solid">PURCHASE RATES</div>
<div class="abs btn btn-line">REFINANCE RATES</div>
<svg class="abs arrow" style="left:22px;background:#3a3a3a" viewBox="0 0 22 22"><path d="M13 6l-5 5 5 5" stroke="#fff" stroke-width="1.6" fill="none"/></svg>
<svg class="abs arrow" style="left:666px;background:#000" viewBox="0 0 22 22"><path d="M9 6l5 5-5 5" stroke="#fff" stroke-width="1.6" fill="none"/></svg>
<div class="dots"><span style="left:339px"></span><span style="left:351px;background:#111"></span><span style="left:363px"></span></div>

<h2 class="abs center section-title" style="top:395px">Mortage Tols</h2>
<p class="abs center section-sub" style="top:425px">Lorem ipsum dolor sit amet, consectetur adipisicing elit, sed do eiusmod tempor.</p>

<div class="abs card" style="left:184px">
  <h3>Mortgage Calculator</h3><div class="rule"></div>
  <p>See how much you can afford by home price.<br>monthly payment, or income</p>
</div>
<div class="abs card" style="left:362px">
  <h3>Home Value Checker</h3><div class="rule"></div>
  <p>Should you refinance? This calculator Breaks<br>Down monthly and lifetime cost</p>
</div>
<svg class="abs tool-icon" style="left:244px" viewBox="0 0 44 44"><g stroke="#fff" stroke-width="1.3" fill="none"><path d="M10 22L22 11l12 11"/><path d="M13 20v13h18V20"/><path d="M17 26h4M19 24v4M24 26h4M17 30l3 2M20 30l-3 2M24 31h4"/></g></svg>
<svg class="abs tool-icon" style="left:421px" viewBox="0 0 44 44"><g stroke="#fff" stroke-width="1.6" fill="none"><path d="M9 22L20 12l11 10"/><path d="M12 20v12h12"/><circle cx="30" cy="29" r="6"/><path d="M27 29l2 2 4-4"/></g></svg>

<section class="abs limits"></section>
<h2 class="abs center section-title" style="top:614px">2019 Mortgage Loan Limits For Conventional, FHA, &amp; VA Loans</h2>
<p class="abs center limits-sub">Mortgage loan limits for every U.S. county, as published by Northgate Home Finance &amp; Keystone Lending Trust, the National Housing Loan Office (NHLO),<br>and the Bureau of Service Member Housing (BSMH)</p>
<div class="abs search-input"></div>
<div class="abs search-btn">SEARCH</div>

<section class="abs connect"></section>
<svg class="abs" style="left:347px;top:753px" width="18" height="34" viewBox="0 0 18 34"><rect x="1" y="1" width="16" height="32" rx="2" stroke="#fff" stroke-width="1" fill="none"/><path d="M1 4h16M1 30h16" stroke="#fff" stroke-width=".8"/></svg>
<h2 class="abs center connect-title">Connet with America’s Lending Experts Today!<br>(888) 555-0142</h2>

<div class="abs town" role="img" aria-label="Line drawing of a row of town houses and church towers"></div>

<footer class="abs footer"></footer>
<div class="abs col" style="left:88px"><h4>LINKS</h4><ul><li>Get a Mortgage Rate Now</li><li>Loan Types</li><li>Homevale Disclosures</li><li>Conforming, VA &amp; FHA Loan Limits</li></ul></div>
<div class="abs divider" style="left:266px"></div>
<div class="abs col" style="left:266px"><h4>COMPANY</h4><ul><li>About Us</li><li>Careers</li><li>Homevale Resouces</li><li>Contact</li></ul></div>
<div class="abs divider" style="left:443px"></div>
<div class="abs col" style="left:443px"><h4>POLICIES</h4><ul><li>Security &nbsp;Policy</li><li>Privacy Policy</li><li>Terms of Use</li><li>Email Policy</li></ul></div>
<div class="abs social" style="left:317px;background:#1c5fb0"></div>
<div class="abs social" style="left:337px;background:#2aa9e6"></div>
<div class="abs social" style="left:357px;background:#c8102e"></div>
<div class="abs social" style="left:378px;background:#ef6a2c"></div>
<div class="abs scroll-top">SCROLL<br>TO TOP</div>
<p class="abs center legal" style="top:1169px">Homevale NMLS #481120. Click here to view our licensing with the NMLS and DRE<br>2009-2020 Copyright Homevale, Inc. All rights reserved. Lending services provided by Homevale, Inc dba Homevale. Rates, program terms and conditions are subject to change without notice.</p>

</body>
</html>
```